Business Card cabinets and cabinets components making company.

the card should be formal and interesting at the same time. The main colors will be black and white.

Font styles to use
Sans Serif

Colors

Designer to choose only greyscale colors for use in the design.

Requirements
Must have
• At least must have the followings:
office phone
cell phone
address
position
name
email
web

```html
<!DOCTYPE html>
<html lang="en">
<head>
<meta charset="utf-8">
<title>Trimfit Business Card</title>
<link href="https://fonts.googleapis.com/css2?family=Roboto:wght@400;500;700;900&display=swap" rel="stylesheet">
<style>
  :root {
    --page: #d9d9d9;
    --ink: #1c1c1c;
    --band: #2b2b2b;
    --paper: #ffffff;
    --text: #222222;
  }
  * { box-sizing: border-box; margin: 0; padding: 0; }
  html, body { width: 1200px; height: 900px; overflow: hidden; }
  body {
    background: var(--page);
    font-family: "Roboto", Arial, sans-serif;
    position: relative;
  }
  .card {
    position: absolute;
    left: 250px;
    width: 700px;
    height: 400px;
    overflow: hidden;
    box-shadow: 0 6px 18px rgba(0,0,0,0.25);
  }
  .card-back { top: 30px; background: var(--ink); }
  .card-front { top: 470px; background: var(--paper); color: var(--text); }

  .card-back .brand {
    position: absolute;
    left: 0; right: 0; top: 150px;
    text-align: center;
    color: var(--paper);
    font-weight: 900;
    font-size: 92px;
    letter-spacing: 1px;
  }

  .card-front .brand {
    position: absolute;
    right: 50px; top: 34px;
    color: var(--ink);
    font-weight: 900;
    font-size: 66px;
  }
  .holder { position: absolute; left: 50px; top: 42px; }
  .holder-name { font-weight: 700; font-size: 24px; letter-spacing: 0.5px; text-transform: uppercase; }
  .holder-role { font-size: 19px; margin-top: 2px; }

  .contacts { position: absolute; left: 72px; top: 112px; list-style: none; }
  .contacts li { display: flex; align-items: center; height: 28px; font-size: 19px; }
  .contacts svg { width: 18px; height: 18px; margin-right: 10px; fill: var(--text); }
  .address { position: absolute; left: 100px; top: 204px; font-size: 19px; line-height: 26px; }

  .swoosh { position: absolute; left: 0; top: 0; width: 700px; height: 400px; }
  .web {
    position: absolute;
    right: 40px; bottom: 34px;
    color: var(--paper);
    font-size: 19px;
    letter-spacing: 0.3px;
  }
</style>
</head>
<body>
  <section class="card card-back">
    <div class="brand">Trimfit</div>
  </section>

  <section class="card card-front">
    <svg class="swoosh" viewBox="0 0 700 400" aria-hidden="true">
      <path d="M0,306 C230,314 360,290 490,215 C580,163 640,132 700,118 L700,400 L0,400 Z" fill="var(--band)"/>
      <path d="M0,326 C235,334 375,308 505,230 C592,177 645,146 700,132 L700,400 L0,400 Z" fill="var(--paper)"/>
      <path d="M0,332 C235,340 380,314 510,236 C596,183 648,152 700,138 L700,400 L0,400 Z" fill="var(--ink)"/>
    </svg>

    <div class="holder">
      <div class="holder-name">Marcus Hale</div>
      <div class="holder-role">Managing Director</div>
    </div>

    <div class="brand">Trimfit</div>

    <ul class="contacts">
      <li>
        <svg viewBox="0 0 24 24"><path d="M6.6 10.8a15.1 15.1 0 0 0 6.6 6.6l2.2-2.2a1 1 0 0 1 1-.25 11.4 11.4 0 0 0 3.6.57 1 1 0 0 1 1 1V20a1 1 0 0 1-1 1A17 17 0 0 1 3 4a1 1 0 0 1 1-1h3.5a1 1 0 0 1 1 1c0 1.25.2 2.45.57 3.57a1 1 0 0 1-.25 1z"/></svg>
        021-480 317 562
      </li>
      <li>
        <svg viewBox="0 0 24 24"><path d="M7 1h10a2 2 0 0 1 2 2v18a2 2 0 0 1-2 2H7a2 2 0 0 1-2-2V3a2 2 0 0 1 2-2zm0 3v14h10V4zm5 15.5a1 1 0 1 0 0 2 1 1 0 0 0 0-2z"/></svg>
        021-480 317 563
      </li>
      <li>
        <svg viewBox="0 0 24 24"><path d="M2 5h20v14H2zm2 2v.5l8 5 8-5V7zm0 2.8V17h16V9.8l-8 5z"/></svg>
        info@trimfitcabinets.com
      </li>
    </ul>

    <div class="address">
      87, Millbrook Workshop Road<br>
      30418, Northvale
    </div>

    <div class="web">www.trimfitcabinets.com</div>
  </section>
</body>
</html>
```